Testosterone clinic billboard

Design billboard for Male Testosterone therapy simple to the point but eye catching.
Contact info for the billboard - Vantoraclinic.com
Phone - 555-274-6180

Target Market(s)

Males with disposable income

Industry/Entity Type

medical

Requirements
Must have
• Testosterone Therapy, Erectile Dysfunction, Male Enhancement
Nice to have
• Simple, easy to read

```html
<!DOCTYPE html>
<html lang="en">
<head>
<meta charset="utf-8">
<title>Vantoraclinic Billboard</title>
<link rel="stylesheet" href="https://fonts.googleapis.com/css2?family=Montserrat:wght@600;700;800&display=swap">
<style>
  :root {
    --page-bg: #e9ecef;
    --purple: #6a1b7a;
    --teal-bright: #1bc4bd;
    --teal-deep: #07706b;
    --white: #ffffff;
  }
  html, body {
    margin: 0;
    width: 1200px;
    height: 1200px;
    overflow: hidden;
    background: var(--page-bg);
    font-family: "Montserrat", Arial, sans-serif;
  }
  .billboard {
    position: absolute;
    left: 40px;
    top: 405px;
    width: 1120px;
    height: 390px;
    overflow: hidden;
    box-shadow: 0 10px 30px rgba(0,0,0,0.18);
  }
  .billboard-shapes {
    position: absolute;
    inset: 0;
    width: 1120px;
    height: 390px;
  }
  .service-list {
    position: absolute;
    left: 345px;
    top: 34px;
    margin: 0;
    padding: 0;
    list-style: none;
  }
  .service-item {
    display: flex;
    align-items: center;
    height: 64px;
    font-size: 42px;
    font-weight: 700;
    letter-spacing: 0.5px;
    color: var(--white);
    white-space: nowrap;
  }
  .service-item::before {
    content: "";
    width: 26px;
    height: 26px;
    border-radius: 50%;
    background: var(--white);
    margin-right: 14px;
    flex: none;
  }
  .service-item .accent {
    color: var(--teal-bright);
    margin-left: 12px;
  }
  .brand-name {
    position: absolute;
    left: 318px;
    top: 310px;
    font-size: 32px;
    font-weight: 700;
    color: var(--purple);
    letter-spacing: 0.5px;
  }
  .contact {
    position: absolute;
    left: 640px;
    top: 290px;
    color: var(--white);
  }
  .contact-phone {
    display: flex;
    align-items: center;
    font-size: 50px;
    font-weight: 700;
    letter-spacing: 1px;
    line-height: 56px;
  }
  .contact-phone svg {
    width: 34px;
    height: 34px;
    margin-right: 10px;
  }
  .contact-web {
    font-size: 26px;
    font-weight: 600;
    letter-spacing: 2.5px;
    margin-top: 4px;
    padding-left: 4px;
  }
</style>
</head>
<body>
  <div class="billboard">
    <svg class="billboard-shapes" viewBox="0 0 1120 390" xmlns="http://www.w3.org/2000/svg">
      <defs>
        <linearGradient id="photoTone" x1="0" y1="0" x2="1" y2="1">
          <stop offset="0" stop-color="#5b6e5a"/>
          <stop offset="0.45" stop-color="#7d8fa8"/>
          <stop offset="1" stop-color="#3f6aa6"/>
        </linearGradient>
      </defs>
      <rect class="panel-purple" x="0" y="0" width="1120" height="390" fill="var(--purple)"/>
      <rect class="band-white" x="0" y="272" width="1120" height="118" fill="var(--white)"/>
      <polygon class="band-teal" points="612,284 1120,270 1120,390 572,390" fill="var(--teal-deep)"/>
      <polygon class="hero-photo" role="img" aria-label="Photo of a worried man in a blue denim shirt holding his head in his hand"
               points="0,0 322,0 262,300 230,390 0,390" fill="url(#photoTone)"/>
    </svg>

    <ul class="service-list">
      <li class="service-item">TESTOSTERONE<span class="accent">THERAPY</span></li>
      <li class="service-item">ERECTILE<span class="accent">DYSFUNCTION</span></li>
      <li class="service-item">MALE<span class="accent">ENHANCEMENT</span></li>
    </ul>

    <div class="brand-name">Vantoraclinic</div>

    <div class="contact">
      <div class="contact-phone">
        <svg viewBox="0 0 24 24" aria-hidden="true">
          <path fill="#ffffff" d="M6.6 10.8c1.4 2.8 3.8 5.1 6.6 6.6l2.2-2.2c.3-.3.7-.4 1-.2 1.1.4 2.3.6 3.6.6.6 0 1 .4 1 1V20c0 .6-.4 1-1 1C10.6 21 3 13.4 3 4c0-.6.4-1 1-1h3.5c.6 0 1 .4 1 1 0 1.3.2 2.5.6 3.6.1.3 0 .7-.2 1l-2.3 2.2z"/>
        </svg>
        555-274-6180
      </div>
      <div class="contact-web">www.vantoraclinic.com</div>
    </div>
  </div>
</body>
</html>
```